Major infrastructure project needs a diagram designed

We need two simple diagrams created on Sydney's current (1) and future (2) intermodal terminal capacity and the number of shipping containers coming out of Kellmere Dock.

Please see attached file for full instructions (Word and PDF attached)

```html
<!DOCTYPE html>
<html lang="en">
<head>
<meta charset="utf-8">
<title>Freight capacity of Sydney's intermodal terminals</title>
<link rel="stylesheet" href="https://fonts.googleapis.com/css2?family=PT+Sans:wght@400;700&display=swap">
<style>
  :root {
    --imex: #f6c75c;
    --interstate: #4fbcc9;
    --regional: #7b7e84;
    --empty: #d9d9d9;
    --arrived: #d9687c;
    --outline: #4a4a4a;
    --label: #3c3c3c;
    --muted: #8a8a8a;
    --brand: #2aa3b4;
    --dash: #6a6a6a;
    --paper: #ffffff;
  }
  * { box-sizing: border-box; margin: 0; padding: 0; }
  html, body { width: 1200px; height: 424px; overflow: hidden; background: var(--paper); }
  body { font-family: "PT Sans", Arial, sans-serif; color: var(--label); position: relative; }

  .panel { position: absolute; top: 0; width: 600px; height: 424px; }
  .panel--current { left: 0; }
  .panel--future { left: 600px; border-left: 1px solid #f0f0f0; }

  .flow-graphics { position: absolute; left: 0; top: 0; width: 600px; height: 424px; }

  .terminal { position: absolute; left: 40px; display: flex; align-items: center; height: 10px; }
  .terminal__name { width: 52px; font-size: 6.5px; line-height: 7px; color: var(--label); font-weight: 400; }
  .terminal__name--lead { font-weight: 700; }
  .stack { display: flex; gap: 3px; }
  .stack-rows { position: absolute; left: 92px; display: flex; flex-direction: column; gap: 3px; }

  .teu { width: 19px; height: 8px; border: 1px solid var(--outline); border-radius: 1px; }
  .teu--imex { background: var(--imex); }
  .teu--interstate { background: var(--interstate); }
  .teu--regional { background: var(--regional) repeating-linear-gradient(90deg, transparent 0 1.5px, rgba(0,0,0,.3) 1.5px 2px); }
  .teu--empty { background: var(--empty); border-color: #9a9a9a; }
  .teu--none { background: var(--paper); border-color: #9a9a9a; }
  .teu--part-s { width: 4px; }
  .teu--part-m { width: 7px; }

  .area-frame { position: absolute; left: 28px; top: 18px; width: 317px; height: 91px; border: 1px dashed var(--dash); }
  .area-frame__note { position: absolute; right: 8px; top: -4px; font-size: 5.5px; line-height: 7px; color: var(--muted); background: var(--paper); padding: 0 2px; white-space: nowrap; }

  .dock-title { position: absolute; font-size: 6.5px; font-weight: 700; color: var(--label); text-transform: uppercase; white-space: nowrap; }
  .flow-note { position: absolute; font-size: 6.5px; line-height: 8px; color: var(--muted); text-align: center; white-space: nowrap; }

  .legend { position: absolute; left: 440px; top: 368px; display: grid; grid-template-columns: 57px 80px; row-gap: 4px; }
  .legend__item { display: flex; align-items: center; gap: 3px; font-size: 5px; color: var(--muted); white-space: nowrap; }
  .legend__item .teu { width: 17px; height: 7px; }
  .legend__item--key { grid-column: 1 / 3; margin-bottom: 4px; }

  .brand { position: absolute; left: 18px; top: 389px; display: flex; align-items: center; gap: 5px; }
  .brand__dot { width: 20px; height: 20px; border-radius: 50%; background: var(--brand); }
  .brand__name { font-size: 5.5px; line-height: 6px; font-weight: 700; color: var(--brand); text-transform: uppercase; }
  .sheet-title { position: absolute; top: 397px; font-size: 10px; font-weight: 400; color: var(--brand); white-space: nowrap; }
  .panel--current .sheet-title { left: 115px; }
  .panel--future .sheet-title { left: 102px; }
</style>
</head>
<body>

<section class="panel panel--current">
  <svg class="flow-graphics" viewBox="0 0 600 424" aria-hidden="true">
    <defs>
      <pattern id="arrived-current" width="22" height="10.5" patternUnits="userSpaceOnUse">
        <rect x="0.5" y="0.5" width="19" height="8" rx="1" fill="#d9687c" stroke="#7a3442" stroke-width="0.8"/>
        <path d="M3 1v7M5 1v7M7 1v7M9 1v7M11 1v7M13 1v7M15 1v7M17 1v7" stroke="#a94459" stroke-width="0.5"/>
      </pattern>
    </defs>
    <g fill="none" stroke="#6a6a6a" stroke-width="0.8" stroke-dasharray="2 2">
      <rect x="478" y="141" width="97" height="112"/>
      <polyline points="478,172 450,172 450,152 410,192 450,232 450,212 478,212"/>
      <path d="M478 282 L523 282 L523 271 L575 271 L575 301 L478 301"/>
      <polyline points="478,282 450,282 450,255 410,290 450,325 450,301 478,301"/>
    </g>
    <g transform="translate(483,146)">
      <rect width="88" height="94.5" fill="url(#arrived-current)"/>
      <rect y="94.5" width="44" height="10.5" fill="url(#arrived-current)"/>
    </g>
    <g transform="translate(483,275)">
      <rect x="44" width="44" height="10.5" fill="url(#arrived-current)"/>
      <rect y="10.5" width="88" height="10.5" fill="url(#arrived-current)"/>
    </g>
  </svg>

  <h2 class="dock-title" style="left:508px; top:121px;">Kellmere Dock</h2>
  <p class="flow-note" style="left:446px; top:184px; width:30px;">distributed<br>by road</p>
  <p class="flow-note" style="left:446px; top:285px; width:30px;">distributed<br>by rail</p>

  <div class="terminal" style="top:224px;"><span class="terminal__name">Yennora</span>
    <div class="stack"><span class="teu teu--imex"></span><span class="teu teu--interstate"></span><span class="teu teu--imex teu--part-s"></span></div></div>
  <div class="terminal" style="top:249px;"><span class="terminal__name">Villawood</span>
    <div class="stack"><span class="teu teu--imex teu--part-m"></span></div></div>
  <div class="terminal" style="top:274px;"><span class="terminal__name">Minto</span>
    <div class="stack"><span class="teu teu--imex"></span><span class="teu teu--imex"></span><span class="teu teu--imex"></span></div></div>
  <div class="terminal" style="top:298px;"><span class="terminal__name">Chullora</span>
    <div class="stack"><span class="teu teu--regional"></span><span class="teu teu--interstate"></span><span class="teu teu--regional"></span><span class="teu teu--interstate"></span></div></div>
  <div class="terminal" style="top:322px;"><span class="terminal__name">Cooks River,<br>St Peters</span>
    <div class="stack"><span class="teu teu--empty"></span><span class="teu teu--empty"></span><span class="teu teu--empty"></span></div></div>
  <div class="terminal" style="top:347px;"><span class="terminal__name">Enfield</span>
    <div class="stack"><span class="teu teu--imex"></span></div></div>

  <div class="legend">
    <div class="legend__item legend__item--key"><span class="teu teu--none"></span>=50000 TEUs p.a.</div>
    <div class="legend__item"><span class="teu teu--imex"></span>IMEX</div>
    <div class="legend__item"><span class="teu teu--empty"></span>empty containers storage</div>
    <div class="legend__item"><span class="teu teu--interstate"></span>interstate</div>
    <div class="legend__item"><span class="teu" style="background:var(--arrived)"></span>arrived to Kellmere Dock</div>
    <div class="legend__item"><span class="teu teu--regional"></span>regional</div>
    <div class="legend__item"><span class="teu teu--none"></span>not investigated</div>
  </div>

  <div class="brand"><span class="brand__dot"></span><span class="brand__name">Ridgeway<br>Intermodal<br>Company</span></div>
  <h1 class="sheet-title">freight capacity of Sydney's intermodal terminals_CURRENT</h1>
</section>

<section class="panel panel--future">
  <svg class="flow-graphics" viewBox="0 0 600 424" aria-hidden="true">
    <defs>
      <pattern id="arrived-future" width="21.5" height="10.5" patternUnits="userSpaceOnUse">
        <rect x="0.5" y="0.5" width="18.5" height="8" rx="1" fill="#d9687c" stroke="#7a3442" stroke-width="0.8"/>
        <path d="M3 1v7M5 1v7M7 1v7M9 1v7M11 1v7M13 1v7M15 1v7M17 1v7" stroke="#a94459" stroke-width="0.5"/>
      </pattern>
    </defs>
    <g fill="none" stroke="#6a6a6a" stroke-width="0.8" stroke-dasharray="2 2">
      <rect x="414" y="77" width="159" height="137"/>
      <polyline points="414,110 382,110 382,90 345,130 382,170 382,150 414,150"/>
      <rect x="414" y="236" width="159" height="98"/>
      <polyline points="414,272 382,272 382,250 345,290 382,330 382,308 414,308"/>
    </g>
    <g transform="translate(418,81)">
      <rect width="150.5" height="126" fill="url(#arrived-future)"/>
      <rect y="126" width="64.5" height="10.5" fill="url(#arrived-future)"/>
    </g>
    <g transform="translate(418,240)">
      <rect x="64.5" width="86" height="10.5" fill="url(#arrived-future)"/>
      <rect y="10.5" width="150.5" height="84" fill="url(#arrived-future)"/>
    </g>
  </svg>

  <div class="area-frame"><span class="area-frame__note">maximum capacity of the area: 1.05 IMEX containers</span></div>

  <h2 class="dock-title" style="left:473px; top:57px;">Kellmere Dock</h2>
  <p class="flow-note" style="left:382px; top:122px; width:30px;">distributed<br>by road</p>
  <p class="flow-note" style="left:382px; top:282px; width:30px;">distributed<br>by rail</p>

  <div class="terminal" style="top:47px;"><span class="terminal__name terminal__name--lead">Moorebank</span></div>
  <div class="stack-rows" style="top:34px;">
    <div class="stack"><span class="teu teu--interstate"></span><span class="teu teu--interstate"></span><span class="teu teu--interstate"></span><span class="teu teu--interstate"></span><span class="teu teu--interstate"></span><span class="teu teu--interstate"></span><span class="teu teu--interstate"></span><span class="teu teu--interstate"></span><span class="teu teu--interstate"></span><span class="teu teu--interstate"></span></div>
    <div class="stack"><span class="teu teu--imex"></span><span class="teu teu--imex"></span><span class="teu teu--imex"></span><span class="teu teu--imex"></span><span class="teu teu--imex"></span><span class="teu teu--imex"></span><span class="teu teu--imex"></span><span class="teu teu--imex"></span><span class="teu teu--imex"></span><span class="teu teu--imex"></span><span class="teu teu--imex"></span></div>
    <div class="stack"><span class="teu teu--imex"></span><span class="teu teu--imex"></span><span class="teu teu--imex"></span><span class="teu teu--imex"></span><span class="teu teu--imex"></span><span class="teu teu--imex"></span><span class="teu teu--imex"></span><span class="teu teu--imex"></span><span class="teu teu--imex"></span><span class="teu teu--imex"></span><span class="teu teu--imex"></span></div>
  </div>

  <div class="terminal" style="top:85px;"><span class="terminal__name">CRESTA</span></div>
  <div class="stack-rows" style="top:81px;">
    <div class="stack"><span class="teu teu--imex"></span><span class="teu teu--imex"></span><span class="teu teu--imex"></span><span class="teu teu--imex"></span><span class="teu teu--imex"></span><span class="teu teu--imex"></span><span class="teu teu--imex"></span><span class="teu teu--imex"></span><span class="teu teu--imex"></span><span class="teu teu--imex"></span></div>
    <div class="stack"><span class="teu teu--imex"></span><span class="teu teu--imex"></span><span class="teu teu--imex"></span><span class="teu teu--imex"></span><span class="teu teu--imex"></span><span class="teu teu--imex"></span><span class="teu teu--imex"></span><span class="teu teu--imex"></span><span class="teu teu--imex"></span><span class="teu teu--imex"></span></div>
  </div>

  <div class="terminal" style="top:127px;"><span class="terminal__name">Eastern Creek</span>
    <div class="stack"><span class="teu teu--imex"></span><span class="teu teu--interstate"></span><span class="teu teu--interstate"></span><span class="teu teu--imex"></span><span class="teu teu--interstate"></span><span class="teu teu--imex"></span><span class="teu teu--imex"></span><span class="teu teu--imex"></span><span class="teu teu--interstate"></span></div></div>
  <div class="terminal" style="top:152px;"><span class="terminal__name">Ingleburn</span>
    <div class="stack"><span class="teu teu--imex"></span><span class="teu teu--imex teu--part-s"></span></div></div>
  <div class="terminal" style="top:176px;"><span class="terminal__name">Leumeah</span>
    <div class="stack"><span class="teu teu--imex"></span></div></div>
  <div class="terminal" style="top:201px;"><span class="terminal__name">Badgerys Creek</span>
    <div class="stack"><span class="teu teu--none"></span><span class="teu teu--none"></span></div></div>
  <div class="terminal" style="top:225px;"><span class="terminal__name">Yennora</span>
    <div class="stack"><span class="teu teu--imex"></span><span class="teu teu--imex"></span><span class="teu teu--imex"></span><span class="teu teu--interstate teu--part-s"></span></div></div>
  <div class="terminal" style="top:249px;"><span class="terminal__name">Villawood</span>
    <div class="stack"><span class="teu teu--imex"></span></div></div>
  <div class="terminal" style="top:274px;"><span class="terminal__name">Minto</span>
    <div class="stack"><span class="teu teu--imex"></span><span class="teu teu--imex"></span><span class="teu teu--imex"></span><span class="teu teu--imex"></span></div></div>
  <div class="terminal" style="top:298px;"><span class="terminal__name">Chullora</span>
    <div class="stack"><span class="teu teu--regional"></span><span class="teu teu--interstate"></span><span class="teu teu--regional"></span><span class="teu teu--interstate"></span><span class="teu teu--regional"></span><span class="teu teu--interstate"></span><span class="teu teu--regional"></span></div></div>
  <div class="terminal" style="top:322px;"><span class="terminal__name">Cooks River,<br>St Peters</span>
    <div class="stack"><span class="teu teu--empty"></span><span class="teu teu--empty"></span><span class="teu teu--empty"></span></div></div>
  <div class="terminal" style="top:347px;"><span class="terminal__name">Enfield</span>
    <div class="stack"><span class="teu teu--imex"></span><span class="teu teu--imex"></span><span class="teu teu--imex"></span><span class="teu teu--imex"></span><span class="teu teu--imex"></span><span class="teu teu--imex"></span></div></div>

  <div class="legend">
    <div class="legend__item legend__item--key"><span class="teu teu--none"></span>=50000 TEUs p.a.</div>
    <div class="legend__item"><span class="teu teu--imex"></span>IMEX</div>
    <div class="legend__item"><span class="teu teu--empty"></span>empty containers storage</div>
    <div class="legend__item"><span class="teu teu--interstate"></span>interstate</div>
    <div class="legend__item"><span class="teu" style="background:var(--arrived)"></span>arrived to Kellmere Dock</div>
    <div class="legend__item"><span class="teu teu--regional"></span>regional</div>
    <div class="legend__item"><span class="teu teu--none"></span>not investigated</div>
  </div>

  <div class="brand"><span class="brand__dot"></span><span class="brand__name">Ridgeway<br>Intermodal<br>Company</span></div>
  <h1 class="sheet-title">freight capacity of Sydney's intermodal terminals_PROPOSED/FUTURE</h1>
</section>

</body>
</html>
```